Oil and Gas Letterhead Design Tweak

Simple letterhead information and design tweak.

Please note, we don't want to change the design or logo of the letterhead only the small changes mentioned below.

We need to change the company name up top to "Northvale Petrotek FZCO"

Also, we need to include in the footer the following information. I have attached an image of roughly how we would like to have it displayed in the footer.

Footer Details:

Northvale Petrotek FZCO,
Unit No. 2378, FZCO Trade Hub, level No. 1, K&P 7, Dubai, United Arab Emirates
Northvale Petrotek FZCO is registered as a free zone company under the rules & regulations of FZCO

Target Market(s)

O&G Market

Industry/Entity Type

Oil And Gas

Font styles to use
Sans Serif

Colors

Designer to choose colors to be used in the design.

Requirements
Must have
• Change the company name to Northvale Petrotek FZCO
• Include the footer on the bottom of the first and continuation page
Should not have
• Should not change the design or logo of the letterhead, only the specified changes mentioned above

```html
<!DOCTYPE html>
<html lang="en">
<head>
<meta charset="utf-8">
<title>Northvale Petrotek FZCO – Letterhead</title>
<link href="https://fonts.googleapis.com/css2?family=Montserrat:wght@400;600;700&display=swap" rel="stylesheet">
<style>
  :root {
    --backdrop: #26a9e0;
    --paper: #ffffff;
    --brand-blue: #1656a8;
    --brand-red: #e61e2a;
    --ink: #231f20;
  }
  * { margin: 0; padding: 0; box-sizing: border-box; }
  html, body { width: 1200px; height: 926px; overflow: hidden; }
  body {
    background: var(--backdrop);
    font-family: "Montserrat", sans-serif;
    color: var(--ink);
    position: relative;
  }
  .sheet {
    position: absolute;
    top: 170px;
    width: 416px;
    height: 587px;
    background: var(--paper);
    overflow: hidden;
  }
  .sheet--first { left: 112px; }
  .sheet--continuation { left: 673px; }
  .band { position: absolute; display: block; }
  .band--top-first { top: 0; left: 0; width: 416px; height: 7px; }
  .band--top-continuation { top: 0; left: 305px; width: 64px; height: 11px; }
  .band--bottom-first { bottom: 0; left: 303px; width: 41px; height: 7px; }
  .band--bottom-continuation { bottom: 0; left: 0; width: 416px; height: 7px; }

  .masthead {
    position: absolute;
    top: 19px;
    left: 112px;
    display: flex;
    align-items: center;
    gap: 7px;
  }
  .masthead__mark {
    width: 10px; height: 10px;
    background: var(--brand-red);
  }
  .masthead__name {
    font-weight: 600;
    font-size: 12.4px;
    letter-spacing: 0.1px;
    color: var(--ink);
  }

  .footer {
    position: absolute;
    font-size: 4.6px;
    line-height: 1;
    color: var(--ink);
  }
  .sheet--first .footer { left: 13px; top: 551px; }
  .sheet--continuation .footer { left: 16px; top: 546px; }
  .footer__company { font-weight: 700; font-size: 5px; margin-bottom: 5px; letter-spacing: 0.1px; }
  .footer__address { display: flex; align-items: center; margin-bottom: 6px; }
  .footer__address span { padding: 0 9px; border-left: 0.9px solid var(--ink); line-height: 8px; }
  .footer__address span:first-child { padding-left: 0; border-left: none; }
  .footer__note { font-size: 4.6px; }

  .signoff {
    position: absolute;
    left: 310px;
    top: 545px;
    width: 56px;
    text-align: center;
    font-weight: 700;
    font-size: 4.4px;
    line-height: 1.15;
    color: var(--ink);
  }
  .signoff__mark {
    width: 8px; height: 8px;
    background: var(--brand-red);
    margin: 0 auto 6px;
  }
</style>
</head>
<body>

  <section class="sheet sheet--first" aria-label="First page letterhead">
    <svg class="band band--top-first" viewBox="0 0 416 7" aria-hidden="true">
      <polygon points="0,0 95,0 90,7 0,7" fill="var(--brand-blue)"/>
      <polygon points="129,0 416,0 416,7 134,7" fill="var(--brand-red)"/>
    </svg>

    <header class="masthead">
      <span class="masthead__mark" aria-hidden="true"></span>
      <span class="masthead__name">NORTHVALE PETROTEK FZCO</span>
    </header>

    <footer class="footer">
      <p class="footer__company">NORTHVALE PETROTEK FZCO</p>
      <p class="footer__address">
        <span>Unit No. 2378</span>
        <span>FZCO Trade Hub</span>
        <span>level No. 1, K&amp;P 7</span>
        <span>Dubai</span>
        <span>United Arab Emirates</span>
      </p>
      <p class="footer__note">Northvale Petrotek FZCO is registered as a free zone company under the rules &amp; regulations of FZCO</p>
    </footer>

    <svg class="band band--bottom-first" viewBox="0 0 41 7" aria-hidden="true">
      <polygon points="4,0 20,0 16,7 0,7" fill="var(--brand-blue)"/>
      <polygon points="24,0 37,0 41,7 20,7" fill="var(--brand-red)"/>
    </svg>
  </section>

  <section class="sheet sheet--continuation" aria-label="Continuation page letterhead">
    <svg class="band band--top-continuation" viewBox="0 0 64 11" aria-hidden="true">
      <polygon points="0,0 33,0 28,11 5,11" fill="var(--brand-blue)"/>
      <polygon points="36,0 64,0 59,11 31,11" fill="var(--brand-red)"/>
    </svg>

    <footer class="footer">
      <p class="footer__company">NORTHVALE PETROTEK FZCO</p>
      <p class="footer__address">
        <span>Unit No. 2378</span>
        <span>FZCO Trade Hub</span>
        <span>level No. 1, K&amp;P 7</span>
        <span>Dubai</span>
        <span>United Arab Emirates</span>
      </p>
      <p class="footer__note">Northvale Petrotek FZCO is registered as a free zone company under the rules &amp; regulations of FZCO</p>
    </footer>

    <div class="signoff">
      <div class="signoff__mark" aria-hidden="true"></div>
      NORTHVALE PETROTEK<br>FZCO
    </div>

    <svg class="band band--bottom-continuation" viewBox="0 0 416 7" aria-hidden="true">
      <polygon points="0,0 309,0 306,7 0,7" fill="var(--brand-blue)"/>
      <polygon points="366,0 416,0 416,7 375,7" fill="var(--brand-red)"/>
    </svg>
  </section>

</body>
</html>
```